Business Card Design Project

we need a business card design for our company: www.plomvik.ch
It's important to include our already existing logo (see website)

```html
<!DOCTYPE html>
<html lang="de">
<head>
<meta charset="utf-8">
<title>Plomvik – Visitenkarte</title>
<link rel="stylesheet" href="https://fonts.googleapis.com/css2?family=Arimo:wght@400;700&display=swap">
<style>
  :root {
    --stage: #4b4443;
    --card: #ffffff;
    --band: #464646;
    --brand-blue: #1f7fcb;
    --ink: #111111;
    --rule: #9a9a9a;
    --shadow: rgba(0, 0, 0, 0.45);
  }
  * { margin: 0; padding: 0; box-sizing: border-box; }
  html, body {
    width: 1200px;
    height: 986px;
    overflow: hidden;
    background: var(--stage);
    font-family: "Arimo", Arial, sans-serif;
  }
  .canvas {
    position: relative;
    width: 1200px;
    height: 986px;
  }
  .card {
    position: absolute;
    width: 620px;
    height: 345px;
    background: var(--card);
    border-radius: 22px;
    overflow: hidden;
    box-shadow: 6px 10px 18px var(--shadow);
  }

  /* Front side */
  .card--front { left: 80px; top: 60px; }
  .card--front .band {
    position: absolute;
    left: 0; right: 0;
    top: 82px;
    height: 182px;
    background: var(--band);
    display: flex;
    align-items: center;
    justify-content: center;
  }
  .wordmark {
    display: flex;
    align-items: center;
    gap: 16px;
    color: var(--brand-blue);
    font-weight: 700;
    letter-spacing: -1px;
  }
  .wordmark__square {
    background: var(--brand-blue);
    flex: none;
  }
  .card--front .wordmark { font-size: 84px; }
  .card--front .wordmark__square { width: 40px; height: 40px; }
  .card--front .website {
    position: absolute;
    left: 0; right: 0;
    top: 286px;
    text-align: center;
    font-size: 20px;
    letter-spacing: 7px;
    color: var(--ink);
  }

  /* Back side */
  .card--back { left: 500px; top: 540px; }
  .card--back .brand-side {
    position: absolute;
    left: 40px;
    top: 84px;
  }
  .card--back .wordmark { font-size: 46px; gap: 10px; }
  .card--back .wordmark__square { width: 22px; height: 22px; }
  .card--back .divider {
    position: absolute;
    left: 300px;
    top: 40px;
    width: 1px;
    height: 265px;
    background: var(--rule);
  }
  .contact {
    position: absolute;
    left: 330px;
    top: 96px;
    color: var(--ink);
  }
  .contact__name {
    font-size: 21px;
    font-weight: 700;
    letter-spacing: 0.5px;
  }
  .contact__role {
    font-size: 17px;
    margin-top: 4px;
  }
  .contact__details {
    margin-top: 30px;
    font-size: 17px;
    line-height: 1.35;
    font-style: normal;
  }
</style>
</head>
<body>
<main class="canvas">
  <section class="card card--front" aria-label="Visitenkarte Vorderseite">
    <div class="band">
      <div class="wordmark">
        <span class="wordmark__square" aria-hidden="true"></span>
        <span class="wordmark__name">Plomvik</span>
      </div>
    </div>
    <p class="website">www.plomvik.ch</p>
  </section>

  <section class="card card--back" aria-label="Visitenkarte Rückseite">
    <div class="brand-side">
      <div class="wordmark">
        <span class="wordmark__square" aria-hidden="true"></span>
        <span class="wordmark__name">Plomvik</span>
      </div>
    </div>
    <div class="divider" aria-hidden="true"></div>
    <div class="contact">
      <p class="contact__name">MK. TAVEN OLRIK</p>
      <p class="contact__role">Software Engineer</p>
      <address class="contact__details">
        Lindenweg 12 - 8050<br>
        Telefon: 044 700 31 58<br>
        Mail: info@plomvik.ch
      </address>
    </div>
  </section>
</main>
</body>
</html>
```